Business Card Design

I am a Special Event Consultant,I arrange and organise Special Events - Product Launches,Sponsorship and Product Displays.

I would like the TRV to be a feature of the design with 'Special Event Services" underneath - keep it very simple but creative using this information. So it is just the letters "TRV" with Event Services underneath.

(Simple Colours - Silver, Black, Grey - no bright colours - We work for Valdoren Kraft,QJX, Tavrelli So it is class and classic.)

Only my Name and mobile on the front.

Industry/Entity Type

Business

Contact Information for Business Card

FRONT
Jo Pettigrew
Tel: 0427 318906

BACK
Email: jo@trvoccasionhire.com.au

1208 Wexley Court,72 Ormond Lane
KELMSTON.Vic.3145.

```html
<!DOCTYPE html>
<html lang="en">
<head>
<meta charset="utf-8">
<title>TRV Special Event Services – Business Card</title>
<link rel="stylesheet" href="https://fonts.googleapis.com/css2?family=Open+Sans:wght@400;600;700&display=swap">
<style>
  :root {
    --backdrop: #3b3b3c;
    --card-black: #121213;
    --card-white: #f4f4f4;
    --silver: #7b7b7d;
    --ink: #1a1a1a;
    --logo-dark: #3a3a3c;
    --rule: #2a2a2a;
  }
  * { margin: 0; padding: 0; box-sizing: border-box; }
  html, body {
    width: 1200px; height: 819px; overflow: hidden;
    background: var(--backdrop);
    font-family: "Open Sans", Arial, sans-serif;
  }
  .canvas {
    position: relative; width: 1200px; height: 819px;
    display: flex; align-items: center; justify-content: center; gap: 40px;
  }
  .card {
    position: relative; width: 540px; height: 309px;
    border-radius: 3px; box-shadow: 0 10px 30px rgba(0,0,0,.35);
  }
  .card--back { background: var(--card-black); }
  .card--front { background: var(--card-white); }

  .brand { position: absolute; }
  .brand__name {
    display: block; font-weight: 700; font-size: 96px;
    line-height: .9; letter-spacing: -4px;
  }
  .brand__tagline {
    display: block; font-weight: 400; font-size: 17px;
    margin-top: 4px; letter-spacing: .2px;
  }
  .card--back .brand { left: 28px; top: 34px; color: var(--silver); }
  .card--front .brand { left: 44px; top: 100px; color: var(--logo-dark); }

  .divider {
    position: absolute; left: 262px; top: 58px;
    width: 1px; height: 194px; background: var(--rule);
  }
  .contact { position: absolute; left: 292px; top: 104px; color: var(--ink); }
  .contact__name { font-weight: 700; font-size: 24px; margin-bottom: 8px; }
  .contact__line {
    display: flex; align-items: center; gap: 7px;
    font-size: 13.5px; line-height: 20px;
  }
  .contact__line svg { width: 12px; height: 12px; flex: none; }
  .contact__address { font-size: 13.5px; line-height: 19px; margin-top: 6px; }
</style>
</head>
<body>
<main class="canvas">
  <section class="card card--back" aria-label="Card back">
    <div class="brand">
      <span class="brand__name">TRV</span>
      <span class="brand__tagline">Special Event Services</span>
    </div>
  </section>

  <section class="card card--front" aria-label="Card front">
    <div class="brand">
      <span class="brand__name">TRV</span>
      <span class="brand__tagline">Special Event Services</span>
    </div>
    <div class="divider"></div>
    <div class="contact">
      <p class="contact__name">Jo Pettigrew</p>
      <p class="contact__line">
        <svg viewBox="0 0 12 12" aria-hidden="true"><path fill="#1a1a1a" d="M1 4c0-2 2-3 5-3s5 1 5 3v1H8.5V3.8C7.8 3.5 4.2 3.5 3.5 3.8V5H1zM2.5 6h7l1 5h-9z"/></svg>
        0427 318906
      </p>
      <p class="contact__line">
        <svg viewBox="0 0 12 12" aria-hidden="true"><rect x="0.5" y="2" width="11" height="8" fill="none" stroke="#1a1a1a"/><path d="M0.5 2l5.5 4.5L11.5 2" fill="none" stroke="#1a1a1a"/></svg>
        jo@trvoccasionhire.com.au
      </p>
      <p class="contact__address">1208 Wexley Court, 72 Ormond Lane<br>KELMSTON.Vic.3145</p>
    </div>
  </section>
</main>
</body>
</html>
```